Pathways to Brightmoor Land Ventures

size of the ad - 8”x 10.75" plus 0.25" bleed
I would like an ad for a magazine that will stand out and make people want to read the ad.
The ad should not be crowded and people reading the ad will be able to read the text.
I would like it to be a creative and modern-day design.
the list of topics should not be the focus of the ad.
the text is attached.
If you decide to use people in the ad then please no ladies.
please note that leave over 1 inch for the bottom of the footer

```html
<!DOCTYPE html>
<html lang="en">
<head>
<meta charset="utf-8">
<title>Pathways to Brightmoor Land Ventures — Course Ad</title>
<link rel="stylesheet" href="https://fonts.googleapis.com/css2?family=Roboto:ital,wght@0,300;0,400;0,700;1,400;1,700&family=Roboto+Condensed:wght@700&display=swap">
<style>
  :root {
    --backdrop: #d6d6d6;
    --photo-light: #b9bfc4;
    --photo-mid: #6d747a;
    --photo-dark: #2b2e31;
    --ink-white: #ffffff;
    --ink-soft: #e4e6e8;
    --ink-muted: #c9ccce;
  }
  * { box-sizing: border-box; margin: 0; padding: 0; }
  html, body {
    width: 1200px; height: 900px; overflow: hidden;
    background: var(--backdrop);
  }
  body { font-family: "Roboto", Arial, sans-serif; color: var(--ink-white); }

  .ad-page {
    position: absolute; left: 280px; top: 20px;
    width: 640px; height: 860px;
    overflow: hidden;
    box-shadow: 0 6px 24px rgba(0,0,0,0.18);
  }
  .ad-photo {
    position: absolute; inset: 0;
    background:
      linear-gradient(180deg, rgba(25,27,29,0.85) 0%, rgba(40,43,46,0.55) 35%, rgba(60,64,68,0.35) 60%, rgba(30,32,34,0.75) 100%),
      linear-gradient(110deg, var(--photo-light) 0%, var(--photo-mid) 45%, var(--photo-dark) 100%);
  }

  .vertical-headline {
    position: absolute;
    left: 0; bottom: 90px;
    width: 760px; height: 118px;
    transform-origin: 0 0;
    transform: rotate(-90deg) translateX(-100%) translateY(0);
    transform: translateY(0) rotate(-90deg);
    transform-origin: left top;
    top: auto;
  }
  .vertical-headline {
    left: 6px; top: 838px;
    transform: rotate(-90deg);
    transform-origin: left top;
    font-family: "Roboto Condensed", "Arial Narrow", sans-serif;
    font-weight: 700;
    font-size: 112px;
    line-height: 118px;
    letter-spacing: 1px;
    color: var(--ink-soft);
    text-transform: uppercase;
    white-space: nowrap;
    text-shadow: 2px 2px 0 rgba(0,0,0,0.45);
  }

  .ad-content {
    position: absolute; left: 200px; top: 70px; right: 40px;
  }
  .course-title {
    font-size: 30px; font-weight: 700; line-height: 1.12;
    text-transform: uppercase; letter-spacing: 0.5px;
  }
  .tagline {
    margin-top: 14px;
    font-size: 18px; font-weight: 300; font-style: italic;
    text-transform: uppercase; letter-spacing: 2px; line-height: 1.2;
    color: var(--ink-soft);
  }
  .session-block { margin-top: 42px; }
  .location { font-size: 24px; font-weight: 700; margin-bottom: 10px; }
  .session-details { list-style: none; font-size: 15px; font-weight: 700; line-height: 1.55; }

  .early-bird { margin-top: 34px; }
  .early-bird-title { font-size: 16px; font-weight: 700; font-style: italic; }
  .early-bird-note { font-size: 15px; color: var(--ink-soft); margin-top: 2px; }

  .topics { margin-top: 56px; }
  .topics-heading { font-size: 14px; font-weight: 700; font-style: italic; margin-bottom: 2px; }
  .topics-list { list-style: none; font-size: 14px; line-height: 1.35; color: var(--ink-muted); }
</style>
</head>
<body>
  <section class="ad-page">
    <div class="ad-photo" role="img" aria-label="Upward view of glass office towers with trees in the lower right, in cool grey tones"></div>

    <div class="vertical-headline">Real Estate Course</div>

    <div class="ad-content">
      <h1 class="course-title">Pathways to Brightmoor<br>Land Ventures</h1>
      <p class="tagline">Investing in knowledge is<br>investing in opportunities.</p>

      <div class="session-block">
        <p class="location">Alderbrook</p>
        <ul class="session-details">
          <li>10 -Tuesday evenings sessions</li>
          <li>Starting Feb.28</li>
          <li>Limited Partial Scholarships</li>
        </ul>
      </div>

      <div class="early-bird">
        <p class="early-bird-title">Early Bird Special</p>
        <p class="early-bird-note">For those that started or would like to go into real estate</p>
      </div>

      <div class="topics">
        <p class="topics-heading">Topics: partial listing</p>
        <ul class="topics-list">
          <li>Real estate investment strategies</li>
          <li>Due diligence</li>
          <li>Financing</li>
          <li>Underwriting</li>
          <li>Property management</li>
          <li>Real estate Legal basics</li>
          <li>Sourcing deals</li>
          <li>Syndication</li>
          <li>Dealing with brokers</li>
          <li>Tax fundamentals</li>
        </ul>
      </div>
    </div>
  </section>
</body>
</html>
```